Delvin & Associates - London New Letting and Property Management Company *

Delvin & Associates LTD is a new company based in London, and works with brand new residential property in the city centre.

We are aiming to have 1000 new properties a year.

We are looking for something modern and minimalistic :
Logo ,Monogram, Paper Head and Business Card.

Target Market(s)

Internation landlords

Industry/Entity Type

Real Estate

Logo Text

Delvin & Associates

Colors

Designer to choose colors to be used in the design.

Requirements
Nice to have
• A particular monogram with "DA"
Should not have
• Little House over the logo

```html
<!DOCTYPE html>
<html lang="en">
<head>
<meta charset="utf-8">
<title>Delvin &amp; Associates LTD – Stationery</title>
<link rel="stylesheet" href="https://fonts.googleapis.com/css2?family=Archivo:wght@800&family=Roboto:wght@400;500;700&display=swap">
<style>
:root{
  --navy:#0c2d57;
  --grey:#8a8a8a;
  --grey-light:#b9b9b9;
  --text:#5c5c5c;
  --paper:#ffffff;
  --bg:#ececec;
}
*{box-sizing:border-box;margin:0;padding:0}
html,body{width:1200px;height:819px;overflow:hidden;background:var(--bg);font-family:"Roboto",Arial,sans-serif;color:var(--text)}
.canvas{position:relative;width:1200px;height:819px}

/* brand lockup */
.brand{display:flex;align-items:center;gap:8px}
.brand-square{width:22px;height:22px;border:2px solid var(--grey)}
.brand-name{font-family:"Archivo",Arial,sans-serif;font-weight:800;color:var(--navy);letter-spacing:.3px;text-transform:uppercase;white-space:nowrap}

/* letterhead */
.letterhead{position:absolute;left:60px;top:28px;width:540px;height:764px;background:var(--paper);box-shadow:0 2px 8px rgba(0,0,0,.12);padding:44px 46px 0}
.lh-top{display:flex;justify-content:space-between;align-items:flex-start}
.lh-top .brand{margin-top:46px}
.lh-top .brand-name{font-size:17px}
.lh-contact{font-size:8px;line-height:1.45}
.lh-contact .company{color:var(--navy);font-weight:700;font-size:9px}
.contact-row{display:flex;align-items:center;gap:5px}
.contact-row svg{width:9px;height:9px;flex:none}
.lh-date{text-align:right;font-size:10px;margin-top:34px}
.recipient{margin-top:28px}
.recipient-name{font-family:"Archivo",Arial,sans-serif;font-weight:800;font-size:17px;color:#4a4a4a}
.recipient-address{font-size:8.5px;line-height:1.35;width:150px;margin-top:2px}
.letter-body p{font-size:10px;line-height:1.6;margin-top:18px;text-align:left}
.signature{margin-top:34px}
.signature-mark{width:120px;height:34px;background:linear-gradient(90deg,#d6d6d6,#eeeeee);border-radius:3px}
.signature-role{font-size:10px;letter-spacing:1.5px;color:var(--grey);margin-top:4px}
.lh-band{position:absolute;left:0;bottom:22px;width:540px;height:20px}
.band-text{font-size:10px;fill:#fff;font-family:"Roboto",Arial,sans-serif}

/* business cards */
.card{position:absolute;width:440px;height:252px;box-shadow:0 2px 8px rgba(0,0,0,.15);overflow:hidden}
.card-front{left:680px;top:120px;background:var(--paper);padding:30px 30px 0}
.card-front .brand{justify-content:flex-end}
.card-front .brand-name{font-size:15px}
.holder{margin-top:34px;border-bottom:1px solid #9a9a9a;padding-bottom:8px;width:100%}
.holder-name{color:var(--navy);font-weight:700;font-size:14px}
.holder-role{font-size:9px;margin-top:2px}
.card-details{display:flex;justify-content:space-between;align-items:flex-end;margin-top:12px;font-size:9.5px;line-height:1.7}
.card-details .contact-row svg{width:10px;height:10px}
.card-address{text-align:right;line-height:1.45}
.card-band{position:absolute;left:0;bottom:0;width:440px;height:16px}
.card-back{left:680px;top:430px;background:var(--navy);display:flex;align-items:center;justify-content:center}
.card-back .brand-square{border-color:#fff;width:26px;height:26px}
.card-back .brand-name{color:#fff;font-size:18px}
</style>
</head>
<body>
<div class="canvas">

  <section class="letterhead">
    <header class="lh-top">
      <div class="brand">
        <span class="brand-square"></span>
        <span class="brand-name">Delvin &amp; Associates LTD</span>
      </div>
      <div class="lh-contact">
        <div class="company">Delvin &amp; Associates LTD</div>
        <div>Suite 12, Harbour House</div>
        <div>Canary Wharf - London, UK</div>
        <div class="contact-row"><svg viewBox="0 0 10 10"><circle cx="5" cy="5" r="5" fill="#0c2d57"/><path d="M3 2.6l1 1-.5.7a3.6 3.6 0 0 0 2.2 2.2l.7-.5 1 1-.8.8C4.8 7.5 2.5 5.2 2.3 3.4z" fill="#fff"/></svg>020-7946-0321</div>
        <div class="contact-row"><svg viewBox="0 0 10 10"><rect x=".5" y="2" width="9" height="6" fill="#0c2d57"/><path d="M.5 2l4.5 3.4L9.5 2" stroke="#fff" stroke-width=".8" fill="none"/></svg>office@delvinassoc.co.uk</div>
        <div class="contact-row"><svg viewBox="0 0 10 10"><circle cx="5" cy="5" r="4.5" fill="#0c2d57"/><path d="M.5 5h9M5 .5c-2.2 2.6-2.2 6.4 0 9M5 .5c2.2 2.6 2.2 6.4 0 9" stroke="#fff" stroke-width=".6" fill="none"/></svg>www.delvinassoc.co.uk</div>
      </div>
    </header>

    <div class="lh-date">Date: 24 April 2017</div>

    <div class="recipient">
      <div class="recipient-name">JOHN DOE</div>
      <div class="recipient-address">Lorem ipsum dolor sit amet, 24 duiselementum dictum amet egestas. Ac eros</div>
    </div>

    <div class="letter-body">
      <p>Lorem ipsum dolor sit amet, duis eu, elementum dictum amet egestas. Ac eros donec venenatis libero, lorem cras rutrum praesent at parturient aliquam, enim suscipit tortor, nec pede metus id, metus tellus at non elit rhoncus. Massa habitasse integer quam tincidunt, vulputate praesent faucibus ut lorem.</p>
      <p>Pellentesque sodales purus. Eleifend integer, ante ipsum. Sed phasellus ut sed, vitae mauris mi vulputate facilisi. In orci urna sagittis augue convallis velit etiam molestie. Ex neque lorem vitae lorem vel massa, sociis facilisis class mus fusce et odio, non enim fringilla ligula. Ante lacus pretium.</p>
      <p>Magna tempor, sit vitae aenean fusce et sociis massa, nascetur morbi. Nunc ac vitae curabitur erat vel nisl. Non litora bibendum sed enim cum varius pellentesque, tellus ligula justo leo eros facilisis, at ornare hendrerit.</p>
    </div>

    <div class="signature">
      <div class="signature-mark" role="img" aria-label="Handwritten signature of John Doe"></div>
      <div class="signature-role">exclusive manager</div>
    </div>

    <svg class="lh-band" viewBox="0 0 540 20" aria-hidden="true">
      <polygon points="0,6 330,6 326,20 0,20" fill="#0c2d57"/>
      <polygon points="336,0 490,0 486,20 332,20" fill="#8a8a8a"/>
      <polygon points="496,0 540,0 540,20 492,20" fill="#0c2d57"/>
      <text class="band-text" x="380" y="14">Tag Line Here</text>
    </svg>
  </section>

  <section class="card card-front">
    <div class="brand">
      <span class="brand-square"></span>
      <span class="brand-name">Delvin &amp; Associates LTD</span>
    </div>
    <div class="holder">
      <div class="holder-name">Tomas Keller</div>
      <div class="holder-role">Director</div>
    </div>
    <div class="card-details">
      <div>
        <div class="contact-row"><svg viewBox="0 0 10 10"><circle cx="5" cy="5" r="5" fill="#0c2d57"/><path d="M3 2.6l1 1-.5.7a3.6 3.6 0 0 0 2.2 2.2l.7-.5 1 1-.8.8C4.8 7.5 2.5 5.2 2.3 3.4z" fill="#fff"/></svg>020-7946-0321</div>
        <div class="contact-row"><svg viewBox="0 0 10 10"><rect x=".5" y="2" width="9" height="6" fill="#0c2d57"/><path d="M.5 2l4.5 3.4L9.5 2" stroke="#fff" stroke-width=".8" fill="none"/></svg>office@delvinassoc.co.uk</div>
        <div class="contact-row"><svg viewBox="0 0 10 10"><circle cx="5" cy="5" r="4.5" fill="#0c2d57"/><path d="M.5 5h9M5 .5c-2.2 2.6-2.2 6.4 0 9M5 .5c2.2 2.6 2.2 6.4 0 9" stroke="#fff" stroke-width=".6" fill="none"/></svg>www.delvinassoc.co.uk</div>
      </div>
      <div class="card-address">Suite 12, Harbour House<br>Canary Wharf - London, UK</div>
    </div>
    <svg class="card-band" viewBox="0 0 440 16" aria-hidden="true">
      <polygon points="0,5 290,5 286,16 0,16" fill="#0c2d57"/>
      <polygon points="296,0 400,0 396,16 292,16" fill="#8a8a8a"/>
      <polygon points="406,0 440,0 440,16 402,16" fill="#0c2d57"/>
    </svg>
  </section>

  <section class="card card-back">
    <div class="brand">
      <span class="brand-square"></span>
      <span class="brand-name">Delvin &amp; Associates LTD</span>
    </div>
  </section>

</div>
</body>
</html>
```